Flyer "Pinch Analysis"-Energy Optimization procedure for Industry

We need a flyer (1xA4 recto/verso )design for a new part of our business.

In Summary: we want to communicate that we are providing "Pinch Analysis" for the industry. It's an energy optimization procedure. We are a cutting edge engineering consulting group.

All details about project in the attached files

Target Market(s)

Engineering

Industry/Entity Type

Business

Font styles to use
Serif

Requirements
Must have
• Finale document in .ai format ready for printing
• More informations in attached files
Nice to have
• See attached files

```html
<!DOCTYPE html>
<html lang="fr">
<head>
<meta charset="utf-8">
<title>Analyse Pinch – Flyer</title>
<link href="https://fonts.googleapis.com/css2?family=Open+Sans:wght@400;600;700&family=Parisienne&display=swap" rel="stylesheet">
<style>
  :root{
    --page-bg:#f4f5f7;
    --paper:#ffffff;
    --navy:#13204f;
    --navy-deep:#0b1538;
    --royal:#1d3fa3;
    --sky:#4cc6f2;
    --sky-light:#8fdcf8;
    --grid:#dcdee2;
    --grid-major:#b9bcc2;
    --curve-hot:#e0262c;
    --curve-cold:#2a3fd4;
    --ink:#222;
    --ink-blue:#1a3a9c;
  }
  *{margin:0;padding:0;box-sizing:border-box}
  html,body{width:1200px;height:1000px;overflow:hidden;background:var(--page-bg)}
  body{position:relative;font-family:"Open Sans",Arial,sans-serif}
  .flyer{position:absolute;left:260px;top:20px;width:681px;height:960px;background:var(--paper);
    box-shadow:6px 6px 14px rgba(0,0,0,.25);overflow:hidden}
  .flyer-art{position:absolute;left:0;top:0}
  .chart-title{position:absolute;top:10px;left:0;width:614px;text-align:center;font-weight:700;font-size:10.5px;text-decoration:underline;color:var(--ink)}
  .axis-label{position:absolute;left:26px;font-size:11px;line-height:12px;color:var(--ink)}
  .axis-title{position:absolute;left:-38px;top:124px;width:100px;text-align:center;transform:rotate(-90deg);font-size:9.5px;font-weight:700;color:var(--ink)}
  .brand{position:absolute;display:flex;align-items:center;gap:8px;font-weight:700;color:var(--sky);white-space:nowrap}
  .brand-mark{width:13px;height:13px;background:var(--sky)}
  .brand--hero{left:8px;top:350px;font-size:20px;line-height:24px}
  .brand--contact{left:233px;top:880px;font-size:15px;line-height:18px}
  .brand--contact .brand-mark{width:10px;height:10px}
  .headline{position:absolute;left:270px;top:402px;width:235px;color:#fff;font-weight:700;font-size:13px;line-height:17px}
  .body-text{position:absolute;color:#fff;font-size:10px;line-height:16.5px}
  .p1{left:149px;top:480px;width:320px}
  .p2{left:84px;top:512px;width:425px}
  .p3{left:32px;top:565px;width:455px;font-size:9px;line-height:12.5px}
  .p3 ul{list-style:none}
  .p3 li::before{content:"• "}
  .p4{left:8px;top:634px;width:500px}
  .p5{left:8px;top:695px;width:380px}
  .script-title{position:absolute;left:500px;top:290px;font-family:"Parisienne",cursive;font-size:30px;line-height:36px;color:#fff;white-space:nowrap}
  .support{position:absolute;left:352px;top:772px;width:325px;color:var(--ink-blue);font-size:9.3px;line-height:13.5px}
  .support p+p{margin-top:6px}
  .contact{position:absolute;left:233px;top:864px;color:var(--ink-blue);font-size:9.5px;line-height:13px;font-weight:700}
  .address{position:absolute;left:214px;top:906px;color:var(--ink-blue);font-size:9.5px;font-weight:700;line-height:13.5px;font-style:normal}
</style>
</head>
<body>
<article class="flyer">
  <svg class="flyer-art" viewBox="0 0 681 960" width="681" height="960">
    <defs>
      <pattern id="grid-minor" width="12" height="11" patternUnits="userSpaceOnUse" x="56" y="56">
        <path d="M12 0V11M0 11H12" fill="none" stroke="var(--grid)" stroke-width="0.7"/>
      </pattern>
      <linearGradient id="navy-fill" x1="0" y1="0" x2="1" y2="1">
        <stop offset="0" stop-color="#1c2d6a"/>
        <stop offset="1" stop-color="#0b1538"/>
      </linearGradient>
      <radialGradient id="photo-plant" cx=".45" cy=".4" r=".7">
        <stop offset="0" stop-color="#eef1f4"/>
        <stop offset=".6" stop-color="#9aa3ad"/>
        <stop offset="1" stop-color="#3d4550"/>
      </radialGradient>
      <radialGradient id="photo-exchanger" cx=".5" cy=".45" r=".7">
        <stop offset="0" stop-color="#c9dff0"/>
        <stop offset=".6" stop-color="#5a86b0"/>
        <stop offset="1" stop-color="#243a58"/>
      </radialGradient>
    </defs>

    <g class="chart">
      <rect x="56" y="56" width="625" height="310" fill="url(#grid-minor)"/>
      <g stroke="var(--grid-major)" stroke-width="1">
        <line x1="56" y1="56" x2="681" y2="56"/>
        <line x1="56" y1="101" x2="681" y2="101"/>
        <line x1="56" y1="144" x2="681" y2="144"/>
        <line x1="56" y1="188" x2="681" y2="188"/>
        <line x1="56" y1="232" x2="681" y2="232"/>
        <line x1="56" y1="276" x2="681" y2="276"/>
        <line x1="56" y1="56" x2="56" y2="366"/>
        <line x1="285" y1="56" x2="285" y2="366"/>
        <line x1="525" y1="56" x2="525" y2="366"/>
      </g>
      <polyline points="227,311 253,298 256,255" fill="none" stroke="var(--curve-hot)" stroke-width="2"/>
      <polyline points="246,324 348,276 380,104 642,101" fill="none" stroke="var(--curve-cold)" stroke-width="2"/>
    </g>

    <path class="wedge-dark" d="M0,205 L318,383 L0,245 Z" fill="var(--navy-deep)"/>
    <path class="wedge-white" d="M0,245 L318,383 L0,493 Z" fill="#fff"/>
    <path d="M0,245 L318,383" stroke="var(--royal)" stroke-width="2"/>

    <path class="panel" d="M0,493 L318,383 C380,330 480,280 681,225 L681,628 C560,660 450,728 360,756 C250,790 120,860 0,905 Z" fill="url(#navy-fill)"/>
    <path d="M0,493 L318,383" stroke="var(--sky)" stroke-width="5"/>
    <path d="M318,383 C380,330 480,280 681,225" fill="none" stroke="var(--sky)" stroke-width="4"/>
    <path d="M0,905 C120,860 250,790 360,756 C450,728 560,660 681,628" fill="none" stroke="var(--sky)" stroke-width="5"/>
    <path d="M0,922 C110,880 220,830 330,795" fill="none" stroke="var(--royal)" stroke-width="7"/>
    <path d="M0,940 C90,908 160,880 220,862" fill="none" stroke="var(--sky-light)" stroke-width="3"/>

    <circle cx="640" cy="445" r="165" fill="var(--navy-deep)"/>
    <circle cx="640" cy="445" r="165" fill="none" stroke="var(--sky)" stroke-width="5"/>
    <circle cx="649" cy="185" r="58" fill="url(#photo-exchanger)" stroke="#fff" stroke-width="4" role="img" aria-label="Photo d'un échangeur de chaleur industriel"/>
    <circle cx="605" cy="455" r="105" fill="url(#photo-plant)" stroke="#fff" stroke-width="5" role="img" aria-label="Photo de tuyauteries dans une installation industrielle"/>
  </svg>

  <div class="chart-title">Hot and Cold Composite Curves</div>
  <span class="axis-label" style="top:50px">160</span>
  <span class="axis-label" style="top:95px">140</span>
  <span class="axis-label" style="top:138px">120</span>
  <span class="axis-label" style="top:182px">100</span>
  <span class="axis-title">Température (°C)</span>

  <div class="brand brand--hero"><span class="brand-mark"></span>Kelvo Engineering</div>
  <div class="script-title">Analyse Pinch</div>

  <h1 class="headline">Analyse Pinch – en route vers la performance opérationnelle et l' efficacité énergétique</h1>

  <p class="body-text p1">La performance opérationnelle et l'efficacité énergétique sont les clés de la réussite de l'industrie de demain.</p>
  <p class="body-text p2">Fort d'une longue expérience dans l'analyse, la conception et la mise en service d'installations industrielles (chimie, alimentaire, pharmacie,…), la société Kelvo utilise l'analyse Pinch dans sa démarche de conception et d'amélioration.</p>
  <div class="body-text p3">
    <p>L'analyse Pinch est une méthode d'analyse systématique développée et appliquée depuis les années 1980; elle permet de répondre aux questions suivantes:</p>
    <ul>
      <li>Quels sont les besoins de chaleur et de froid minimaux de mon procédé</li>
      <li>Quel est mon potentiel de réduction de consommation énergétique</li>
      <li>Quel est la solution technique présentant les coûts minimaux entre investissements et économies</li>
    </ul>
  </div>
  <p class="body-text p4">L'amélioration de l'efficacité énergétique est liée directement à l'exploitation des potentiels de récupération du procédé. Des potentiels de diminution de la consommation de 10 à 30% sont usuels. Nous pouvons également améliorer les performances opérationnelles en analysant vos méthodes de fabrication.</p>
  <p class="body-text p5">L'analyse Pinch est aussi bien adaptée pour les PME que pour les grandes entreprises dont les procédés sont exploités de manière continue ou discontinue (batch).</p>

  <div class="support">
    <p>Etant donné les objectifs énergétiques de la confédération, l'office fédérale de l'énergie (OFEN) soutient les analyses Pinch à hauteur de 35% pour les procédés continus et de 60% pour les procédés discontinus (batch).</p>
    <p>Pour tous compléments d'informations et pour savoir si une analyse Pinch est justifiée dans votre cas, nous vous conseillons avec plaisir.</p>
  </div>

  <div class="contact">Contact: Luc Marend, Paul Decosterd</div>
  <div class="brand brand--contact"><span class="brand-mark"></span>Kelvo Engineering</div>
  <address class="address">Kelvo SA<br>Rue des Forges 14<br>CH-1900 Valmont</address>
</article>
</body>
</html>
```